Succession & Estate Planning firm needs a double-sided one page client handout

We need a client hand-out that highlights the top 10 Reasons to get a Pension Plan. It will need the 10 reasons as headings, with a short description of each reason (attached Word doc). It should communicate that a Pension Plan is flexible and provides security. Our usual client is a business owner/medical professional/entrepreneur. Have a look at our website for more info about our business www.quorvane.ca Our logo colours are 83c242, 3b3839, d5d5d5 We like clean, modern, info-graphics, not too cluttered, not too loudWe would like the ability to update the text/content ourselves, in the future.

```html
<!DOCTYPE html>
<html lang="en">
<head>
<meta charset="utf-8">
<title>Quorvane – Top 10 Reasons to Get a Pension Plan</title>
<link rel="stylesheet" href="https://fonts.googleapis.com/css2?family=Montserrat:wght@400;500;600&family=Oswald:wght@500;600&display=swap">
<style>
:root{
  --green:#83c242;
  --charcoal:#3b3839;
  --silver:#d5d5d5;
  --row:#e4e4e4;
  --icon-bg:#8a8a8c;
  --paper:#ffffff;
  --stage:#efefed;
  --ink:#2c2a2b;
}
*{box-sizing:border-box;margin:0;padding:0}
html,body{width:1200px;height:1200px;overflow:hidden;background:var(--stage);font-family:"Montserrat",sans-serif;color:var(--ink)}
.page{position:absolute;top:234px;width:518px;height:733px;background:var(--paper);overflow:hidden;box-shadow:0 2px 10px rgba(0,0,0,.18)}
.page--front{left:66px}
.page--back{left:617px}

/* front */
.hero{position:absolute;left:0;top:0;width:518px;height:485px;
  background:linear-gradient(180deg,#fbfbf7 0%,#f4f4e6 22%,#e9eec0 42%,#b9cf78 60%,#7d9a45 74%,#5a4a3a 86%,#3e3026 100%)}
.brand{position:absolute;left:0;right:0;text-align:center;font-weight:500;color:var(--charcoal)}
.page--front .brand{top:70px;font-size:38px}
.banner{position:absolute;left:0;top:485px;width:518px;height:48px;background:var(--green);
  font-family:"Oswald",sans-serif;font-weight:600;color:#fff;font-size:25px;text-align:center;line-height:48px;letter-spacing:.3px}
.intro{position:absolute;left:25px;right:25px;top:545px}
.intro h2{font-weight:500;font-size:20px;text-align:center;color:var(--ink);margin-bottom:12px}
.intro p{font-size:9.2px;line-height:11.6px;text-align:justify;color:#333}
.footer{position:absolute;left:0;bottom:0;width:100%;height:50px;background:var(--charcoal)}
.footer__green{position:absolute;top:0;height:36px;background:var(--green)}
.page--front .footer__green{left:228px;right:0;clip-path:polygon(0 0,100% 0,100% 100%,18px 100%)}
.addr{position:absolute;left:24px;top:10px;color:#fff;font-size:9.6px;line-height:12.5px;font-weight:500;display:flex;gap:6px}
.contact{position:absolute;top:0;height:36px;display:flex;align-items:center;gap:6px;color:#fff;font-size:10px;font-weight:500}

/* back */
.header{position:absolute;left:0;top:0;width:518px;height:118px;background:radial-gradient(ellipse at 50% 30%,#4d4b4c 0%,#343233 70%,#2b292a 100%)}
.page--back .brand{top:40px;font-size:28px;color:#fff}
.title-bar{position:absolute;left:0;top:118px;width:518px;height:34px;background:var(--green);
  font-family:"Oswald",sans-serif;font-weight:500;font-size:19.5px;line-height:34px;text-align:center;color:#fff}
.title-bar em{font-style:normal;color:var(--charcoal)}
.reasons{position:absolute;left:24px;top:158px;width:470px;list-style:none}
.reason{position:relative;height:46px;margin-bottom:6.2px}
.reason__body{position:absolute;left:0;top:0;width:379px;height:46px;background:var(--row);padding:4px 10px 0 83px}
.reason__num{position:absolute;left:0;top:12px;width:68px;height:34px;background:var(--green);color:#fff;
  clip-path:polygon(0 0,72% 0,100% 100%,0 100%);font-weight:500;font-size:22px;line-height:34px;padding-left:22px}
.reason__title{font-size:8.2px;font-weight:600;margin-bottom:3px;color:#222}
.reason__text{font-size:5.9px;line-height:7.6px;text-align:justify;color:#444}
.reason__icon{position:absolute;right:0;top:0;width:82px;height:46px;background:var(--icon-bg);display:flex;align-items:center;justify-content:center}
.reason__icon svg{width:34px;height:34px;fill:none;stroke:#fff;stroke-width:2.2;stroke-linecap:round;stroke-linejoin:round}
.page--back .footer{height:42px}
.page--back .footer__green{left:184px;right:0;height:30px;clip-path:polygon(0 0,100% 0,100% 100%,12px 100%)}
.web{position:absolute;left:184px;right:0;top:0;height:30px;line-height:30px;text-align:center;color:#fff;font-size:11.5px;letter-spacing:4.5px}
.phone{position:absolute;left:28px;top:0;height:42px;display:flex;align-items:center;gap:8px;color:#fff;font-size:14px;font-weight:500}
</style>
</head>
<body>

<section class="page page--front">
  <div class="hero" role="img" aria-label="Young green seedlings growing from stacks of gold coins in soil, soft sunlit background"></div>
  <div class="brand">Quorvane</div>
  <div class="banner">THE TOP 10 REASONS TO GET A PENSION PLAN</div>
  <div class="intro">
    <h2>Succession &amp; Estate Planning</h2>
    <p>Succession and estate planning can often seem like a puzzle. Due to the numerous complex issues that are intertwined in succession and estate planning, beginning the process can be a daunting task. That is why we are here to help. We will walk with you through each piece of the puzzle and see how it will all work together in your unique situation. By working collaboratively with our client’s team of professional advisors, we are passionate about helping our clients clarify their goals for estate, succession and philanthropy planning, to give them the confidence to move forward, and take action in making these dreams a reality.</p>
  </div>
  <footer class="footer">
    <div class="footer__green"></div>
    <div class="addr">
      <svg width="12" height="11" viewBox="0 0 12 11"><path d="M6 0 0 5h2v6h3V7h2v4h3V5h2z" fill="#83c242"/></svg>
      <span>118 – 402 Birch Avenue<br>Saskatoon, Saskatchewan, S7K 2L4</span>
    </div>
    <div class="contact" style="left:258px">
      <svg width="12" height="12" viewBox="0 0 24 24" fill="none" stroke="#fff" stroke-width="2.2"><path d="M5 3h4l2 5-2.5 1.5a11 11 0 0 0 6 6L16 13l5 2v4a2 2 0 0 1-2 2A17 17 0 0 1 3 5a2 2 0 0 1 2-2z"/></svg>
      <span>(306) 555-0142</span>
    </div>
    <div class="contact" style="left:378px">
      <svg width="12" height="12" viewBox="0 0 24 24" fill="none" stroke="#fff" stroke-width="2"><circle cx="12" cy="12" r="10"/><path d="M2 12h20M12 2c3 3 3 17 0 20M12 2c-3 3-3 17 0 20"/></svg>
      <span>www.quorvane.ca</span>
    </div>
  </footer>
</section>

<section class="page page--back">
  <header class="header">
    <div class="brand">Quorvane</div>
  </header>
  <div class="title-bar"><em>Top 10 Reasons</em> Why an FPP Serves Your Family Enterprise</div>

  <ol class="reasons">
    <li class="reason"><div class="reason__body"><div class="reason__num">1</div><div class="reason__title">Create Significant Deductions</div><p class="reason__text">The FPP creates significant tax deductions, which can be used to keep the business under the small business rate or applied to the high rate, a bigger bang for the buck.</p></div>
      <div class="reason__icon"><svg viewBox="0 0 34 34"><rect x="4" y="7" width="22" height="13" rx="1"/><circle cx="15" cy="13.5" r="3"/><circle cx="25" cy="24" r="6"/><path d="M25 21v6"/></svg></div></li>
    <li class="reason"><div class="reason__body"><div class="reason__num">2</div><div class="reason__title" style="margin-top:10px">Deliberate, Planned, Future Income</div><p class="reason__text">An income for beyond the last day at the office.</p></div>
      <div class="reason__icon"><svg viewBox="0 0 34 34"><circle cx="18" cy="11" r="7"/><path d="M18 7v8M4 24h6l6 3 12-5"/><path d="M4 29h8"/></svg></div></li>
    <li class="reason"><div class="reason__body"><div class="reason__num">3</div><div class="reason__title">Past Buy Back</div><p class="reason__text">Most owners invest, first, in the business. The FPP offers the ability to go back and recover lost years when they did not buy RRSPs...and pass the tax savings onto their company.</p></div>
      <div class="reason__icon"><svg viewBox="0 0 34 34"><path d="M6 17a11 11 0 1 0 4-8.5"/><path d="M5 5v5h5M17 10v7l5 3"/></svg></div></li>
    <li class="reason"><div class="reason__body"><div class="reason__num">4</div><div class="reason__title">Creditor Proof</div><p class="reason__text">All Assets held in an FPP are creditor proof, including RRSPs, &amp; planned pension contributions receive “super-priority” status, which rank above the claims of secured creditors, like major commercial lenders &amp; banks.</p></div>
      <div class="reason__icon"><svg viewBox="0 0 34 34"><rect x="12" y="6" width="16" height="20" rx="1"/><path d="M16 20l8-9"/><circle cx="16.5" cy="12" r="1.5"/><circle cx="23.5" cy="19" r="1.5"/><path d="M6 14v12h6"/></svg></div></li>
    <li class="reason"><div class="reason__body"><div class="reason__num">5</div><div class="reason__title">Flexibility</div><p class="reason__text">a. Owners know that cash flows can swing wildly with the business cycle. An FPP offers the flexibility to flip between DB and DC accounts in order to conserve cash, smooth income during volatile years, &amp; recover assets when things improve.</p></div>
      <div class="reason__icon"><svg viewBox="0 0 34 34"><path d="M17 30V6M13 10l4-4 4 4M17 20l-10-6M7 19v-5h5M17 20l10-6M27 19v-5h-5"/></svg></div></li>
    <li class="reason"><div class="reason__body"><div class="reason__num">6</div><div class="reason__title">Preserve the Lifetime Capital Gains Exemption</div><p class="reason__text">Create $1.6 Million++ of Tax Free Capital Gains. The significant deductions created in an FPP can be used to purify a corporation with passive assets, which can help preserve the shareholders’ lifetime capital gains exemption.</p></div>
      <div class="reason__icon"><svg viewBox="0 0 34 34"><rect x="6" y="14" width="22" height="14" rx="1"/><circle cx="17" cy="21" r="3.5"/><path d="M18 10v-2M21 10v-4M24 10v-6M27 10v-8"/></svg></div></li>
    <li class="reason"><div class="reason__body"><div class="reason__num">7</div><div class="reason__title">Intergenerational Wealth Transfer</div><p class="reason__text">Unlike RRSPs that eventually trigger a taxable disposition upon death, an FPP has the ability to pass, tax deferred, to the next generation of family business owners.</p></div>
      <div class="reason__icon"><svg viewBox="0 0 34 34"><rect x="6" y="11" width="22" height="12" rx="1"/><circle cx="17" cy="17" r="3"/><path d="M22 6h-9M15 4l-2 2 2 2M12 28h9M19 26l2 2-2 2"/></svg></div></li>
    <li class="reason"><div class="reason__body"><div class="reason__num">8</div><div class="reason__title" style="margin-top:10px">All Ages</div><p class="reason__text">An FPP can benefit all entrepreneurs between ages 18-71.</p></div>
      <div class="reason__icon"><svg viewBox="0 0 34 34"><circle cx="11" cy="7" r="3"/><circle cx="23" cy="7" r="3"/><path d="M8 13h6v9h-1v8M8 13v9h1v8M20 13h6l2 10h-3v7M20 13l-2 10h3v7"/></svg></div></li>
    <li class="reason"><div class="reason__body"><div class="reason__num">9</div><div class="reason__title">Conserve the Small Business Deduction</div><p class="reason__text">Investment income inside an FPP grows tax exempt and does not create passive income as outlined under the 2018 “Halvorsen Measures”. Therefore, business owners that redirect corporate resources to fund their pension assets will not jeopardize their low corporate tax rate on profits &amp; in associated companies.</p></div>
      <div class="reason__icon"><svg viewBox="0 0 34 34"><circle cx="18" cy="12" r="8"/><path d="M20.5 9h-4a2 2 0 0 0 0 4h3a2 2 0 0 1 0 4h-4M18 7v12M4 26h7l6 3 12-5"/></svg></div></li>
    <li class="reason"><div class="reason__body"><div class="reason__num">10</div><div class="reason__title">Broader Investment Options</div><p class="reason__text">An FPP allows entrepreneurs to invest in what they like: real estate, other businesses and/or franchises, private equity, public equity, exempt markets, etc. The possibilities are up to the imagination of the entrepreneur &amp; their advisors.</p></div>
      <div class="reason__icon"><svg viewBox="0 0 34 34"><path d="M6 29v-6M11 29v-9M16 29v-11M21 29v-14M26 29v-17M5 18l7-5 5 3 11-10M23 6h5v5"/></svg></div></li>
  </ol>

  <footer class="footer">
    <div class="footer__green"></div>
    <div class="phone">
      <svg width="14" height="14" viewBox="0 0 24 24" fill="none" stroke="#fff" stroke-width="2.2"><path d="M5 3h4l2 5-2.5 1.5a11 11 0 0 0 6 6L16 13l5 2v4a2 2 0 0 1-2 2A17 17 0 0 1 3 5a2 2 0 0 1 2-2z"/></svg>
      <span>(306) 555-0142</span>
    </div>
    <div class="web">www.quorvane.ca</div>
  </footer>
</section>

</body>
</html>
```